Brenmoor Group needs a business card

I would like the card to be simple but modern and elegant.
I like black and white.
or black and gold.
we are a private finance lender and also are involved in property and property developments.

please look at the business card photos i provided i would like B.G only one one side and all the other details on the other side use fonts that tie in with my theme.

Industry/Entity Type

Finance

Contact Information for Business Card

Brenmoor Group (B.G) Callum Brenmoor M: 0418396152 E: callumbren@quivomail.com

Font styles to use
Other font styles liked:
• Use fonts that would reflect our business

Colors
000000
ffffff

Requirements
Must have
• one side of details
• other side has either B.G or Brenmoor Group like in the photos provided

```html
<!DOCTYPE html>
<html lang="en">
<head>
<meta charset="utf-8">
<title>Brenmoor Group — Business Card</title>
<link rel="stylesheet" href="https://fonts.googleapis.com/css2?family=Montserrat:wght@400;600;700&family=Questrial&family=Open+Sans:wght@400&display=swap">
<style>
  :root {
    --ink: #000000;
    --paper: #ffffff;
    --gold: #d4972f;
    --gold-faint: rgba(255, 255, 255, 0.14);
    --font-brand: "Montserrat", sans-serif;
    --font-name: "Questrial", sans-serif;
    --font-label: "Open Sans", sans-serif;
  }
  * { box-sizing: border-box; margin: 0; padding: 0; }
  html, body {
    width: 1200px;
    height: 520px;
    overflow: hidden;
    background: var(--paper);
  }
  .canvas {
    position: relative;
    width: 1200px;
    height: 520px;
  }

  /* Back side */
  .card-back {
    position: absolute;
    left: 7px;
    top: 41px;
    width: 565px;
    height: 295px;
    background: var(--ink);
  }
  .back-lockup {
    position: absolute;
    left: 0;
    right: 0;
    top: 72px;
    display: flex;
    align-items: center;
    justify-content: center;
    gap: 18px;
  }
  .back-lockup .brand-mark {
    width: 104px;
    height: 104px;
    border: 4px solid var(--paper);
    border-radius: 50%;
    flex: none;
  }
  .back-lockup .brand-name {
    font-family: var(--font-brand);
    font-weight: 600;
    font-size: 30px;
    line-height: 1.1;
    color: var(--paper);
  }
  .card-back .holder-name {
    position: absolute;
    left: 0;
    right: 0;
    top: 210px;
    text-align: center;
    font-family: var(--font-name);
    font-size: 27px;
    letter-spacing: 2px;
    color: var(--paper);
  }

  /* Front side */
  .card-front {
    position: absolute;
    left: 629px;
    top: 34px;
    width: 512px;
    height: 331px;
    background: var(--gold);
    border: 6px solid var(--ink);
    overflow: hidden;
  }
  .front-lockup {
    position: absolute;
    left: 26px;
    top: 24px;
    font-family: var(--font-brand);
    font-weight: 700;
    font-size: 30px;
    line-height: 1;
    color: var(--paper);
  }
  .brand-shade {
    position: absolute;
    left: 200px;
    top: 120px;
    width: 240px;
    height: 240px;
    border-radius: 50%;
    background: var(--gold-faint);
  }
  .contact-block {
    position: absolute;
    right: 34px;
    top: 112px;
    width: 350px;
    text-align: right;
    color: var(--ink);
  }
  .contact-block .holder-name {
    text-align: left;
    font-family: var(--font-name);
    font-size: 28px;
    letter-spacing: 1.5px;
    line-height: 1;
    padding-left: 10px;
  }
  .contact-block .name-rule {
    height: 4px;
    background: var(--ink);
    margin: 8px -34px 0 0;
  }
  .contact-block .role {
    font-family: var(--font-brand);
    font-weight: 400;
    font-size: 21px;
    margin-top: 12px;
    padding-right: 10px;
  }
  .contact-block .phone {
    font-family: var(--font-brand);
    font-weight: 700;
    font-size: 16px;
    margin-top: 30px;
  }
  .contact-block .email {
    display: flex;
    justify-content: flex-end;
    align-items: center;
    gap: 6px;
    font-family: var(--font-brand);
    font-weight: 400;
    font-size: 19px;
    margin-top: 10px;
  }
  .email-icon { width: 24px; height: 24px; flex: none; }

  /* Side labels */
  .side-label {
    position: absolute;
    top: 420px;
    font-family: var(--font-label);
    font-size: 58px;
    line-height: 1;
    color: var(--ink);
    transform: translateX(-50%);
  }
  .side-label.back { left: 297px; }
  .side-label.front { left: 928px; top: 428px; }
</style>
</head>
<body>
<main class="canvas">
  <section class="card-back" aria-label="Card back">
    <div class="back-lockup">
      <span class="brand-mark" aria-hidden="true"></span>
      <span class="brand-name">Brenmoor<br>Group</span>
    </div>
    <p class="holder-name">CALLUM BRENMOOR</p>
  </section>

  <section class="card-front" aria-label="Card front">
    <div class="brand-shade" aria-hidden="true"></div>
    <p class="front-lockup">Brenmoor Group</p>
    <div class="contact-block">
      <p class="holder-name">CALLUM BRENMOOR</p>
      <div class="name-rule"></div>
      <p class="role">Finance</p>
      <p class="phone">M: 0418396152</p>
      <p class="email">
        <svg class="email-icon" viewBox="0 0 26 26" aria-hidden="true">
          <circle cx="13" cy="13" r="11" fill="none" stroke="#000" stroke-width="2"/>
          <circle cx="13" cy="13" r="4.5" fill="none" stroke="#000" stroke-width="2"/>
          <path d="M17.5 9v5.5a2.5 2.5 0 0 0 5 0V13" fill="none" stroke="#000" stroke-width="2"/>
        </svg>
        <span>callumbren@quivomail.com</span>
      </p>
    </div>
  </section>

  <p class="side-label back">back</p>
  <p class="side-label front">front</p>
</main>
</body>
</html>
```